Product Designer Business Card

Small product design, engineering and prototyping firm in need of a clean, professional business card design. To support our 3D design and drawing services, we offer 3D printing, molding, and casting of plastics, silicones, resins, etc. Our logo can still be modified/changed if necessary. The red/orange color is preferred, but may be substituted with blue or green, potentially. Either way, the colour of the logo should be match/compliment colors used throughout the design. One thought is to have the logo/contact info on one side, with the other side describing services offered, like with a small icon of 3D printer, molding, casting, and computer with a 3D model on-screen.
Industry/Entity Type
Mechanical Engineering
Contact Information for Business Card
Company: Halvick Design
Phone: 613-582-4179
Email: myles@halvickdesign.ca

```html
<!DOCTYPE html>
<html lang="en">
<head>
<meta charset="utf-8">
<title>Halvick Design – Business Card</title>
<link href="https://fonts.googleapis.com/css2?family=Orbitron:wght@500;700&family=Exo+2:wght@400;600&display=swap" rel="stylesheet">
<style>
  :root {
    --bg: #2b2f36;
    --red: #d9241f;
    --red-dark: #8e1512;
    --red-deep: #b01a16;
    --white: #ffffff;
    --ink: #2a2a2a;
    --shadow: rgba(0,0,0,0.45);
  }
  * { box-sizing: border-box; margin: 0; padding: 0; }
  html, body { width: 1200px; height: 900px; overflow: hidden; }
  body {
    background: var(--bg);
    font-family: "Exo 2", sans-serif;
    position: relative;
  }
  .card {
    position: absolute;
    overflow: hidden;
    border-radius: 4px;
    box-shadow: 0 18px 40px var(--shadow);
  }

  /* Front */
  .card-front {
    left: 110px; top: 152px;
    width: 340px; height: 595px;
    background: var(--white);
  }
  .front-shapes { position: absolute; inset: 0; }
  .brand {
    position: absolute; left: 118px; top: 70px;
    display: flex; align-items: center; gap: 10px;
  }
  .brand-dot {
    width: 30px; height: 30px; border-radius: 50%;
    background: var(--red);
  }
  .brand-name {
    font-family: "Orbitron", sans-serif; font-weight: 700;
    font-size: 34px; color: var(--red);
    letter-spacing: 2px;
  }
  .contact {
    position: absolute; left: 36px; top: 222px;
  }
  .person-name {
    font-family: "Orbitron", sans-serif; font-weight: 700;
    font-size: 22px; color: var(--red);
  }
  .person-role {
    font-size: 13px; color: var(--red); margin: 2px 0 14px;
  }
  .contact-line {
    display: flex; align-items: center; gap: 8px;
    font-family: "Orbitron", sans-serif; font-weight: 500;
    font-size: 12.5px; color: var(--ink);
    margin-bottom: 8px;
  }
  .contact-icon {
    width: 18px; height: 18px; border-radius: 3px;
    background: var(--red-deep);
    display: flex; align-items: center; justify-content: center;
  }

  /* Back */
  .card-back {
    left: 500px; top: 152px;
    width: 595px; height: 340px;
    background:
      linear-gradient(155deg, rgba(255,255,255,0.08) 0 40%, rgba(0,0,0,0.12) 40% 100%),
      linear-gradient(135deg, var(--red) 0%, var(--red-dark) 50%, var(--red) 100%);
  }
  .services {
    position: absolute; inset: 0;
    display: flex; justify-content: space-around; align-items: center;
    padding: 0 30px;
  }
  .service { display: flex; flex-direction: column; align-items: center; gap: 16px; }
  .service-badge {
    width: 130px; height: 130px; border-radius: 50%;
    background: radial-gradient(circle at 40% 35%, #ffffff 55%, #e2e2e2 100%);
    box-shadow: 0 6px 14px rgba(0,0,0,0.35);
    display: flex; align-items: center; justify-content: center;
  }
  .service-label {
    font-family: "Orbitron", sans-serif; font-weight: 500;
    font-size: 14px; letter-spacing: 2px; color: var(--white);
  }
</style>
</head>
<body>

<section class="card card-front">
  <svg class="front-shapes" width="340" height="595" viewBox="0 0 340 595">
    <defs>
      <radialGradient id="ringShade" cx="0.6" cy="0.6" r="0.6">
        <stop offset="0.45" stop-color="#6e0f0c"/>
        <stop offset="1" stop-color="#e02a22"/>
      </radialGradient>
      <radialGradient id="halfShade" cx="0.2" cy="0.5" r="0.8">
        <stop offset="0" stop-color="#8e1512"/>
        <stop offset="1" stop-color="#e02a22"/>
      </radialGradient>
    </defs>
    <circle cx="0" cy="150" r="90" fill="url(#halfShade)"/>
    <circle cx="310" cy="500" r="200" fill="url(#ringShade)"/>
    <circle cx="340" cy="530" r="95" fill="#ffffff"/>
  </svg>

  <div class="brand">
    <span class="brand-dot"></span>
    <span class="brand-name">Halvick</span>
  </div>

  <div class="contact">
    <p class="person-name">Myles Tanner</p>
    <p class="person-role">Managing director</p>
    <p class="contact-line">
      <span class="contact-icon">
        <svg width="10" height="12" viewBox="0 0 10 12"><rect x="1" y="0.5" width="8" height="11" rx="1.5" fill="none" stroke="#fff" stroke-width="1.3"/><circle cx="5" cy="9.3" r="0.9" fill="#fff"/></svg>
      </span>
      613-582-4179
    </p>
    <p class="contact-line">
      <span class="contact-icon">
        <svg width="12" height="9" viewBox="0 0 12 9"><rect x="0.6" y="0.6" width="10.8" height="7.8" fill="none" stroke="#fff" stroke-width="1.2"/><path d="M0.6 0.6 L6 5 L11.4 0.6" fill="none" stroke="#fff" stroke-width="1.2"/></svg>
      </span>
      myles@halvickdesign.ca
    </p>
  </div>
</section>

<section class="card card-back">
  <div class="services">
    <div class="service">
      <div class="service-badge">
        <svg width="74" height="74" viewBox="0 0 74 74" fill="none" stroke="#c41d18" stroke-width="4" stroke-linejoin="round">
          <rect x="34" y="4" width="30" height="20" rx="3"/>
          <path d="M42 24 L40 31 L48 24"/>
          <circle cx="20" cy="34" r="6"/>
          <path d="M8 56 v-8 a12 10 0 0 1 24 0 v8 z"/>
          <circle cx="52" cy="44" r="6"/>
          <path d="M40 68 v-8 a12 10 0 0 1 24 0 v8 z"/>
        </svg>
      </div>
      <span class="service-label">CONSULT</span>
    </div>
    <div class="service">
      <div class="service-badge">
        <svg width="78" height="74" viewBox="0 0 78 74" fill="none" stroke="#c41d18" stroke-width="4" stroke-linejoin="round" stroke-linecap="round">
          <rect x="4" y="10" width="62" height="42" rx="3"/>
          <path d="M28 52 v10 M42 52 v10 M22 64 h26"/>
          <path d="M34 40 L68 8 L74 12 L40 44 Z"/>
        </svg>
      </div>
      <span class="service-label">DESIGN</span>
    </div>
    <div class="service">
      <div class="service-badge">
        <svg width="74" height="74" viewBox="0 0 74 74" fill="none" stroke="#c41d18" stroke-width="3.5" stroke-linejoin="round">
          <rect x="8" y="8" width="58" height="60" rx="2"/>
          <path d="M8 22 h58"/>
          <rect x="30" y="22" width="14" height="12"/>
          <path d="M37 34 v6"/>
          <rect x="26" y="50" width="22" height="8"/>
          <path d="M16 62 h42"/>
        </svg>
      </div>
      <span class="service-label">PROTOTYPE</span>
    </div>
  </div>
</section>

</body>
</html>
```